Header Card Design for Marine Tool Product

We package up our small tools in bags. A nice header card would finish the look.
* Bag is 4" wide. Header Card should be 4x4, folded to 4x2
* Back of card should have 2.25x1.25 area for our part number sticker.
* Design to reinforce the brand and add (perception of) quality to the product.

Brand Website: keelworks.net

Target Market(s)

Boat Mechanics/Boat owners

Industry/Entity Type

```html
<!DOCTYPE html>
<html lang="en">
<head>
<meta charset="utf-8">
<title>Keelworks – Header Card</title>
<link rel="stylesheet" href="https://fonts.googleapis.com/css2?family=Poppins:wght@400;600&display=swap">
<style>
  :root {
    --navy: #0f1f4b;
    --navy-deep: #0a1838;
    --navy-line: #1f3466;
    --cyan: #2fc4d8;
    --strip: #3f8fc6;
    --white: #ffffff;
    --sticker: #f3f1e6;
    --ink: #3a3a3a;
    --page: #eef0f3;
  }
  * { box-sizing: border-box; margin: 0; padding: 0; }
  html, body { width: 980px; height: 1200px; overflow: hidden; }
  body {
    background: var(--page);
    font-family: "Poppins", sans-serif;
    color: var(--white);
    position: relative;
  }
  .card-panel {
    position: absolute;
    left: 110px;
    width: 760px;
    height: 380px;
    background: var(--navy);
    overflow: hidden;
  }
  .card-front { top: 150px; }
  .card-back { top: 670px; }

  .scene-art {
    position: absolute;
    background: linear-gradient(135deg, var(--navy-line), var(--navy) 70%);
    opacity: 0.75;
  }
  .card-front .art-right { right: 0; top: 0; width: 200px; height: 360px; }
  .card-front .art-left { left: 0; top: 190px; width: 220px; height: 170px; }
  .card-front .hill {
    position: absolute; left: 330px; top: 230px; width: 320px; height: 260px;
    border-radius: 50%; background: var(--navy-deep);
  }
  .bottom-strip {
    position: absolute; left: 0; bottom: 0; width: 100%; height: 20px;
    background: var(--strip);
  }

  .born-in {
    position: absolute; top: 82px; left: 0; width: 100%;
    text-align: center; font-size: 16px; letter-spacing: 18px;
    padding-left: 18px;
    color: var(--cyan); font-weight: 400;
  }
  .brand-lockup {
    position: absolute; display: flex; align-items: center; gap: 14px;
  }
  .card-front .brand-lockup { top: 150px; left: 0; width: 100%; justify-content: center; }
  .brand-dot { width: 30px; height: 30px; border-radius: 50%; background: var(--cyan); }
  .brand-name { font-weight: 600; font-size: 54px; line-height: 1.2; color: var(--white); }

  .card-back .art-bottom { left: 360px; top: 200px; width: 400px; height: 180px; }
  .card-back .brand-lockup { top: 56px; left: 56px; }
  .card-back .brand-name { font-size: 34px; }
  .card-back .brand-dot { width: 22px; height: 22px; }

  .contact { position: absolute; left: 56px; top: 170px; }
  .contact-address { font-size: 17px; line-height: 1.4; font-weight: 400; }
  .contact-phone, .contact-web { font-size: 24px; font-weight: 600; line-height: 1.3; }
  .contact-phone { margin-top: 16px; }

  .part-sticker {
    position: absolute; right: 56px; top: 40px; width: 300px; height: 170px;
    background: var(--sticker); border-radius: 12px; color: var(--ink);
    padding: 24px 28px;
    display: flex; flex-direction: column;
  }
  .part-sticker p { line-height: 1.25; }
  .part-number { font-size: 34px; font-weight: 600; letter-spacing: 1px; }
  .part-code { font-size: 12px; margin-top: auto; }
  .part-desc { font-size: 10px; margin-top: 2px; }
  .part-cond { font-size: 12px; margin-top: 2px; }
</style>
</head>
<body>
  <section class="card-panel card-front">
    <div class="scene-art art-right" role="img" aria-label="Faint line drawing of a harbor crane and ship"></div>
    <div class="scene-art art-left" role="img" aria-label="Faint line drawing of a crane boom with hooks and a barge"></div>
    <div class="hill"></div>
    <p class="born-in">BORN IN</p>
    <div class="brand-lockup">
      <span class="brand-dot"></span>
      <span class="brand-name">Keelworks</span>
    </div>
    <div class="bottom-strip"></div>
  </section>

  <section class="card-panel card-back">
    <div class="scene-art art-bottom" role="img" aria-label="Faint line drawing of a harbor crane and bridge truss"></div>
    <div class="brand-lockup">
      <span class="brand-dot"></span>
      <span class="brand-name">Keelworks</span>
    </div>
    <div class="contact">
      <p class="contact-address">418 Harbor Row, Suite 12,<br>Port Wren SC, 29000</p>
      <p class="contact-phone">(555)010-2287</p>
      <p class="contact-web">keelworks.net</p>
    </div>
    <div class="part-sticker">
      <p class="part-number">KWT0217</p>
      <p class="part-code">X00K3LW9QP</p>
      <p class="part-desc">Keel Pin Spanner KWT0217 - 36mm x 5mm</p>
      <p class="part-cond">New</p>
    </div>
  </section>
</body>
</html>
```